Brindle Works Australia Website

Brindle Works Australia (BWA) is a Industrial, Mining & Transport Services provider in Australia. We require a website that is both pc and mobile freindly. The website will be used to both present our company services and give us exposure in a crowded market. The main page of the website will have a snapshot of who BWA is and its from this page that the user can click to enter the area of interest ie. Industrial, Mining and Transport. A disticted logo can be used to indicate the area in question.<br/>Within the industrial, Mining and the Transport services pages will need list and description of services that are provided, current customer lists and news pages.<br/>The website will need a contacts page so prospective customers can get in contact with BWA.<br/>The website design will require a user freindly back end so future updates and ammendments can be carriedout by less experienced people within the BWA business.

Target Market(s)

Industrial, Mining and Transport Services provider markets

Coding

Number of Pages Required

5+ page

Font styles to use
Sans Serif

Colors
00a990

Requirements
Must have
• Ability to build servises with in services. because the main service area is only the main service with in each service group there is alot of smaller services / tasks.
• Key wording for easy seach engine capabilities. The website will need to be search engine freindly.

```html
<!DOCTYPE html>
<html lang="en">
<head>
<meta charset="utf-8">
<title>Brindle Works Australia — Mining &amp; Transport Services</title>
<link href="https://fonts.googleapis.com/css2?family=Montserrat:wght@700;800&family=Barlow:wght@400;500;600;700&display=swap" rel="stylesheet">
<style>
:root{
  --green:#0d6b3a;
  --green-dark:#0a5a30;
  --ink:#222222;
  --text:#6b6b6b;
  --charcoal:#2f2b29;
  --footer:#1d1f1f;
  --white:#ffffff;
  --line:#cfcfcf;
}
*{box-sizing:border-box;margin:0;padding:0}
html,body{width:1200px;height:4146px;overflow:hidden}
body{position:relative;background:var(--white);font-family:"Barlow",sans-serif;color:var(--ink)}
.abs{position:absolute}
.heading{font-family:"Montserrat",sans-serif;font-weight:800;color:var(--ink);letter-spacing:-.5px}
.rule{position:absolute;height:4px;width:52px;background:var(--green)}
.btn{position:absolute;background:var(--green);color:#fff;font-family:"Montserrat",sans-serif;font-weight:700;display:flex;align-items:center;justify-content:center;text-transform:uppercase}

/* top bar */
.topbar{top:0;left:0;width:1200px;height:38px;background:var(--green)}
.topbar .social{left:110px;top:13px;display:flex;gap:10px}
.topbar .social span{width:11px;height:11px;border-radius:50%;background:#fff;display:block}
.topbar .login{left:688px;top:11px;color:#fff;font-size:13px;font-weight:600}
.topbar .divider{left:828px;top:8px;width:1px;height:22px;background:rgba(255,255,255,.5)}
.topbar .call{left:858px;top:9px;color:#fff;font-size:12px;font-weight:600}
.topbar .call b{font-size:16px;font-weight:700}

/* header */
.header{top:38px;left:0;width:1200px;height:88px;background:#fff;box-shadow:0 1px 3px rgba(0,0,0,.08)}
.brand{left:100px;top:22px;display:flex;align-items:center;gap:10px}
.brand .mark{width:44px;height:44px;background:var(--green)}
.brand .name{font-family:"Barlow",sans-serif;font-weight:700;color:var(--green);font-size:17px;line-height:17px;text-transform:uppercase;width:120px}
.tagline{left:330px;top:24px;font-family:"Barlow",sans-serif;font-weight:700;font-size:17px;line-height:18px;text-align:right;text-transform:uppercase;color:var(--ink)}
.nav{left:618px;top:32px;display:flex;gap:38px;font-size:13px;font-weight:700;text-transform:uppercase}
.nav a{color:var(--ink);text-decoration:none;position:relative}
.nav a.active{color:var(--green)}
.nav a.active::after{content:"";position:absolute;left:-4px;right:-4px;bottom:-14px;height:3px;background:var(--green)}
.nav .search{width:14px;height:14px}

/* hero */
.hero{top:126px;left:0;width:1200px;height:622px}
.hero .panel{left:286px;top:122px;width:628px;height:251px;background:rgba(70,70,80,.55)}
.hero h1{left:0;width:1200px;top:158px;text-align:center;font-family:"Montserrat",sans-serif;font-weight:800;color:#fff;font-size:49px;line-height:52px;text-transform:uppercase}
.hero .sub{left:0;width:1200px;top:272px;text-align:center;font-family:"Montserrat",sans-serif;font-weight:700;color:#fff;font-size:28px}
.hero .btn{left:526px;top:328px;width:146px;height:48px;font-size:14px}
.dots{display:flex;gap:8px}
.dots span{width:12px;height:12px;border-radius:50%;background:#fff;display:block}
.hero .dots{left:564px;top:489px}

/* welcome */
.welcome h2{left:111px;top:815px;font-size:38px}
.welcome .rule{left:111px;top:871px}
.welcome p{left:111px;top:898px;width:460px;font-size:13.5px;line-height:25.8px;color:var(--text);text-align:justify}
.welcome .btn{left:111px;top:1100px;width:147px;height:50px;font-size:14px}
.video-frame{left:610px;top:817px;width:487px;height:325px;background:var(--green)}
.video{left:600px;top:827px;width:491px;height:323px;background:linear-gradient(135deg,#8a8478 0%,#5a5348 45%,#c49a3a 70%,#2b2a28 100%)}
.play{left:800px;top:944px;width:90px;height:90px;border-radius:50%;background:rgba(13,107,58,.85)}

/* features */
.features{top:1231px;left:0;width:1200px;height:643px}
.features h2{right:690px;top:82px;color:#fff;font-size:38px;text-align:right}
.features .rule{left:462px;top:134px;background:#fff}
.feature{right:690px;width:410px;text-align:right;color:#fff}
.feature h3{font-family:"Barlow",sans-serif;font-weight:700;font-size:18px;text-transform:uppercase;margin-bottom:4px}
.feature p{font-size:13.5px;line-height:24px;color:#e8e8e8}
.feature-icon{left:552px;width:84px;height:84px;border-radius:50%;background:var(--green);border:4px solid #fff;display:flex;align-items:center;justify-content:center}

/* services */
.services h2{left:0;width:1200px;top:1948px;text-align:center;font-size:38px}
.services .rule{left:574px;top:2006px}
.card{width:310px;height:340px}
.card .photo{left:0;top:0;width:310px;height:305px}
.card .caption{left:26px;top:205px;width:258px;height:135px;color:#fff;text-align:center}
.card .caption h3{position:absolute;top:52px;width:100%;font-size:17px;font-weight:700;text-transform:uppercase}
.card .caption p{position:absolute;top:82px;width:100%;font-size:13.5px;line-height:22px;padding:0 14px}
.services .dots{left:574px;top:2452px}
.services .dots span{background:#aaa;width:13px;height:13px}
.services .dots span.on{background:#222}

/* news */
.news{top:2537px;left:0;width:1200px;height:643px}
.news h2{left:116px;top:112px;color:var(--ink);font-size:38px}
.news .rule{left:116px;top:162px}
.news .intro{left:116px;top:184px;width:330px;font-size:13.5px;line-height:26px;color:#333}
.arrow{top:38px;width:44px;height:44px;display:flex;align-items:center;justify-content:center}
.news-card{top:111px;width:312px;height:437px;background:#fff}
.news-card .photo{left:0;top:0;width:312px;height:212px}
.news-card .date{left:0;top:0;width:67px;height:70px;background:var(--green);color:#fff;padding:8px 8px}
.news-card .date b{display:block;font-size:24px;font-weight:700;line-height:26px}
.news-card .date small{font-size:11px;font-weight:600}
.news-card h3{left:30px;top:232px;width:270px;font-size:17.5px;line-height:35px;font-weight:700;text-transform:uppercase}
.news-card p{left:30px;top:310px;width:260px;font-size:13px;line-height:25.5px;color:var(--text)}
.news-card a{left:32px;top:397px;font-size:13px;color:var(--green)}
.news-card.faded::after{content:"";position:absolute;inset:0;background:rgba(40,36,30,.55)}

/* contact */
.contact .map{left:300px;top:3170px;width:600px;height:560px}
.contact h2{left:0;width:1200px;top:3280px;text-align:center;font-size:38px}
.contact .rule{left:574px;top:3334px}
.field{background:#fff;border:1px solid var(--line);font-size:12.5px;color:#8a8a8a;padding:0 20px;display:flex;align-items:center;gap:6px}
.field.tall{align-items:flex-start;padding-top:18px}
.contact .btn{left:511px;top:3566px;width:181px;height:55px;font-size:15px;gap:6px}

/* footer */
.footer{top:3772px;left:0;width:1200px;height:374px}
.f-icon{top:3835px;width:94px;height:94px;border-radius:50%;background:var(--green);display:flex;align-items:center;justify-content:center}
.f-text{top:3858px;color:#fff}
.f-text h4{font-size:16px;font-weight:700}
.f-text p{font-size:17px;line-height:24px}
.f-text p.small{font-size:13px;line-height:24px}
.f-links{left:0;width:1200px;top:3972px;text-align:center;color:#fff;font-size:14px}
.f-links span{margin:0 10px}
.f-social{left:528px;top:4018px;display:flex;gap:5px}
.f-social span{width:33px;height:33px;border-radius:50%;border:1.5px solid #fff;display:block}
.copyright{left:0;width:1200px;top:4069px;text-align:center;color:#fff;font-size:13.5px}
</style>
</head>
<body>

<!-- Top bar -->
<div class="abs topbar">
  <div class="abs social"><span></span><span></span><span></span><span></span></div>
  <div class="abs login">&#9679; Login / Register</div>
  <div class="abs divider"></div>
  <div class="abs call">&#9742; Call us Today : <b>+1 555 014 2290</b></div>
</div>

<!-- Header -->
<header class="abs header">
  <div class="abs brand"><span class="mark"></span><span class="name">Brindle Works Australia</span></div>
  <div class="abs tagline">Mining &amp; Transport<br>Services</div>
  <nav class="abs nav">
    <a class="active">Home</a><a>About</a><a>Services</a><a>News</a><a>Contact Us</a>
    <svg class="search" viewBox="0 0 14 14"><circle cx="6" cy="6" r="4.5" fill="none" stroke="#222" stroke-width="2"/><line x1="9.2" y1="9.2" x2="13" y2="13" stroke="#222" stroke-width="2.2"/></svg>
  </nav>
</header>

<!-- Hero -->
<section class="abs hero">
  <svg class="abs" style="left:0;top:0" width="1200" height="622" role="img" aria-label="Photo of a harbour city skyline with an opera house and a sailboat on blue water">
    <defs>
      <linearGradient id="heroSky" x1="0" y1="0" x2="0" y2="1">
        <stop offset="0" stop-color="#a9c4e6"/><stop offset=".45" stop-color="#7d93ad"/>
        <stop offset=".62" stop-color="#5c6f80"/><stop offset=".7" stop-color="#2f5e9e"/>
        <stop offset="1" stop-color="#1c4e93"/>
      </linearGradient>
    </defs>
    <polygon points="0,0 1200,0 1200,622 0,558" fill="url(#heroSky)"/>
  </svg>
  <div class="abs panel"></div>
  <h1 class="abs">Brindle Works<br>Australia</h1>
  <div class="abs sub">Mining &amp; Transport Services</div>
  <div class="btn">Get Started</div>
  <div class="abs dots"><span></span><span></span><span></span><span></span></div>
</section>

<!-- Welcome -->
<section class="welcome">
  <h2 class="abs heading">WELCOME</h2>
  <div class="rule"></div>
  <p class="abs">Lorem ipsum dolor sit amet, consectetur adipiscing elit, sed do eiusmod tempor incididunt ut labore et dolore magna aliqua. Ut enim ad minim veniam, quis nostrud exercitation ullamco laboris nisi ut aliquip ex ea commodo consequat. Duis aute irure dolor in reprehenderit in voluptate velit esse cillum dolore eu fugiat nulla pariatur Excepteur sint occaecat cupidatat non proident, sunt in culpa qui officia deserunt mollit anim id est laborum.</p>
  <div class="btn">Read More &raquo;</div>
  <div class="abs video-frame"></div>
  <div class="abs video" role="img" aria-label="Video still of a yellow haul truck at a mine site"></div>
  <svg class="abs play" viewBox="0 0 90 90"><polygon points="37,30 62,45 37,60" fill="#fff"/></svg>
</section>

<!-- Features -->
<section class="abs features">
  <svg class="abs" style="left:0;top:0" width="1200" height="643">
    <defs>
      <linearGradient id="featDark" x1="0" y1="0" x2="1" y2="1">
        <stop offset="0" stop-color="#4a4340"/><stop offset="1" stop-color="#2c2826"/>
      </linearGradient>
      <linearGradient id="featPhoto" x1="0" y1="0" x2="0" y2="1">
        <stop offset="0" stop-color="#d8d6d2"/><stop offset=".5" stop-color="#8d7a66"/>
        <stop offset=".8" stop-color="#c0895a"/><stop offset="1" stop-color="#6d5140"/>
      </linearGradient>
    </defs>
    <polygon points="0,0 1200,0 1200,587 0,643" fill="#2a2624"/>
    <polygon points="0,0 594,40 594,643 0,643" fill="url(#featDark)" role="img" aria-label="Dim photo of a mine site with haul trucks"/>
    <polygon points="594,40 1200,80 1200,587 594,643" fill="url(#featPhoto)" role="img" aria-label="Photo of a loaded mining dump truck on a dirt road"/>
  </svg>
  <h2 class="abs heading">OUR FEATURES</h2>
  <div class="rule"></div>
  <div class="abs feature" style="top:180px"><h3>Workforce Shuttles</h3><p>Lorem ipsum dolor sit amet, consectetur adipiscing elit, sed do eiusmod tempor incididunt ut labore et dolore magna aliqua. Ut enim ad minim</p></div>
  <div class="abs feature" style="top:317px"><h3>Contractor Transport</h3><p>Lorem ipsum dolor sit amet, consectetur adipiscing elit, sed do eiusmod tempor incididunt ut labore et dolore magna aliqua. Ut enim ad minim</p></div>
  <div class="abs feature" style="top:454px"><h3>Transport Scheduling</h3><p>Lorem ipsum dolor sit amet, consectetur adipiscing elit, sed do eiusmod tempor incididunt ut labore et dolore magna aliqua. Ut enim ad minim</p></div>
  <div class="abs feature-icon" style="top:170px"><svg width="40" height="40" viewBox="0 0 40 40"><path d="M6 24a14 14 0 0 1 28 0z" fill="#fff"/><rect x="4" y="24" width="32" height="4" fill="#fff"/><circle cx="20" cy="33" r="4" fill="none" stroke="#fff" stroke-width="2.5"/></svg></div>
  <div class="abs feature-icon" style="top:307px"><svg width="42" height="40" viewBox="0 0 42 40"><rect x="10" y="8" width="12" height="12" fill="none" stroke="#fff" stroke-width="2.5"/><rect x="6" y="20" width="26" height="8" fill="#fff"/><rect x="4" y="30" width="28" height="6" rx="3" fill="none" stroke="#fff" stroke-width="2"/><path d="M32 22l7 4v8h-5" fill="none" stroke="#fff" stroke-width="2.5"/></svg></div>
  <div class="abs feature-icon" style="top:444px"><svg width="42" height="40" viewBox="0 0 42 40"><rect x="4" y="20" width="16" height="10" fill="#fff"/><rect x="2" y="31" width="22" height="5" rx="2.5" fill="none" stroke="#fff" stroke-width="2"/><path d="M18 22L28 10l10 6v8" fill="none" stroke="#fff" stroke-width="3"/><path d="M34 24h6l-3 5z" fill="#fff"/></svg></div>
</section>

<!-- Services -->
<section class="services">
  <h2 class="abs heading">OUR SERVICES</h2>
  <div class="rule"></div>

  <div class="abs card" style="left:111px;top:2044px">
    <div class="abs photo" role="img" aria-label="Photo of an industrial plant with storage tanks at dusk" style="background:linear-gradient(180deg,#4f5f86 0%,#c48a5c 35%,#3b4a66 60%,#6e7f92 100%)"></div>
    <svg class="abs" style="left:26px;top:205px" width="258" height="135"><polygon points="0,40 258,0 258,135 0,135" fill="#2b2726"/></svg>
    <div class="abs caption"><h3>Industrial</h3><p>Lorem ipsum dolor sit amet, consectetur adipiscing elit, sed</p></div>
  </div>

  <div class="abs card" style="left:444px;top:2044px">
    <div class="abs photo" role="img" aria-label="Photo of a lit mining tunnel with rail tracks" style="background:radial-gradient(circle at 50% 55%,#e9dcc1 0%,#b49a78 35%,#6d5a45 75%,#3b3128 100%)"></div>
    <svg class="abs" style="left:26px;top:205px" width="258" height="135"><polygon points="0,40 258,0 258,135 0,135" fill="var(--green)"/></svg>
    <div class="abs caption"><h3>Mining</h3><p>Lorem ipsum dolor sit amet, consectetur adipiscing elit, sed</p></div>
  </div>

  <div class="abs card" style="left:777px;top:2044px">
    <div class="abs photo" role="img" aria-label="Photo of a yellow mining dump truck under a blue sky" style="background:linear-gradient(180deg,#a9c8e4 0%,#cfd8df 40%,#c8962e 60%,#6b6a66 100%)"></div>
    <svg class="abs" style="left:26px;top:205px" width="258" height="135"><polygon points="0,40 258,0 258,135 0,135" fill="#2b2726"/></svg>
    <div class="abs caption"><h3>Transport Services</h3><p>Lorem ipsum dolor sit amet, consectetur adipiscing elit, sed</p></div>
  </div>

  <div class="abs dots"><span></span><span class="on"></span><span></span></div>
</section>

<!-- News -->
<section class="abs news">
  <svg class="abs" style="left:0;top:0" width="1200" height="643">
    <defs>
      <linearGradient id="newsLeft" x1="0" y1="0" x2="1" y2="1">
        <stop offset="0" stop-color="#e7ddc2"/><stop offset=".45" stop-color="#c7a250"/>
        <stop offset=".8" stop-color="#8d7342"/><stop offset="1" stop-color="#4f4430"/>
      </linearGradient>
      <linearGradient id="newsRight" x1="0" y1="0" x2="1" y2="1">
        <stop offset="0" stop-color="#3f3831"/><stop offset="1" stop-color="#2a2520"/>
      </linearGradient>
    </defs>
    <polygon points="0,0 1200,0 1200,643 0,643" fill="#e6e6e6"/>
    <polygon points="0,40 598,40 598,603 0,643" fill="url(#newsLeft)" role="img" aria-label="Photo of a yellow haul truck driving through a dusty mine pit"/>
    <polygon points="598,40 1200,0 1200,563 598,603" fill="url(#newsRight)" role="img" aria-label="Dark faded photo of heavy machinery"/>
  </svg>
  <h2 class="abs heading">LATEST NEWS</h2>
  <div class="rule"></div>
  <p class="abs intro">Lorem ipsum dolor sit amet, consectetur adipiscing elit, sed do eiusmod tempor incididunt ut labore et dolore magna aliqua. Ut enim ad nostrud</p>

  <div class="abs arrow" style="left:999px;background:#8f8f8f"><svg width="14" height="14" viewBox="0 0 14 14"><path d="M9 2L4 7l5 5" fill="none" stroke="#fff" stroke-width="2"/></svg></div>
  <div class="abs arrow" style="left:1043px;background:#fff"><svg width="14" height="14" viewBox="0 0 14 14"><path d="M5 2l5 5-5 5" fill="none" stroke="#222" stroke-width="2"/></svg></div>

  <article class="abs news-card" style="left:634px">
    <div class="abs photo" role="img" aria-label="Photo of two workers in hard hats and high-visibility vests at a site" style="background:linear-gradient(160deg,#eef1f4 0%,#c9ccd0 45%,#e38a2c 75%,#6a6c70 100%)"></div>
    <div class="abs date"><b>12</b><small>Dec, 2019</small></div>
    <h3 class="abs">Lorem ipsum dolor sit am et, consectetur</h3>
    <p class="abs">Lorem ipsum dolor sit amet, cons ecte tu r adipiscing elit, sed do eiusmod tem por incididunt ut labore</p>
    <a class="abs"><u>Read more</u></a>
  </article>

  <article class="abs news-card faded" style="left:965px;width:235px;overflow:hidden">
    <div class="abs photo" role="img" aria-label="News photo" style="background:#7a7a7a"></div>
    <div class="abs date"><b>12</b><small>Dec, 2019</small></div>
    <h3 class="abs" style="width:300px">Lorem ipsum dolor sit am et, consectetur</h3>
    <p class="abs">Lorem ipsum dolor sit amet, cons ecte tu r adipiscing elit, sed do eiusmod tem por incididunt ut labore</p>
    <a class="abs"><u>Read more</u></a>
  </article>
</section>

<!-- Contact -->
<section class="contact">
  <div class="abs map" role="img" aria-label="Pale green map of Australia" style="background:radial-gradient(ellipse at 50% 45%,#cfe6d9 0%,#cfe6d9 55%,rgba(207,230,217,0) 72%)"></div>
  <h2 class="abs heading">CONTACT US</h2>
  <div class="rule"></div>
  <div class="abs field" style="left:187px;top:3359px;width:405px;height:56px">&#9679; First name*</div>
  <div class="abs field" style="left:608px;top:3359px;width:405px;height:56px">&#9679; Last name*</div>
  <div class="abs field" style="left:187px;top:3428px;width:405px;height:56px">&#9993; Email Address*</div>
  <div class="abs field tall" style="left:608px;top:3428px;width:405px;height:125px">&#9675; Message*</div>
  <div class="abs field" style="left:187px;top:3496px;width:405px;height:57px">&#9742; Phone*</div>
  <div class="btn"><svg width="14" height="14" viewBox="0 0 14 14"><path d="M13 1L1 6l4 2 1 5 2-3 3 2z" fill="#fff"/></svg>Submit</div>
</section>

<!-- Footer -->
<footer>
  <div class="abs footer" role="img" aria-label="Dark photo of a city skyline at dusk" style="background:linear-gradient(180deg,#2a2d2d 0%,#1c1e1e 60%,#151616 100%)"></div>

  <div class="abs f-icon" style="left:148px"><svg width="40" height="40" viewBox="0 0 40 40"><path d="M12 6l6 7-3 4c2 4 5 7 9 9l4-3 7 6-4 5C19 33 7 21 6 10z" fill="none" stroke="#fff" stroke-width="2.5" stroke-linejoin="round"/></svg></div>
  <div class="abs f-text" style="left:260px"><h4>Phone :</h4><p>+1 555 014 2290</p></div>

  <div class="abs f-icon" style="left:445px"><svg width="40" height="40" viewBox="0 0 40 40"><path d="M20 32s-9-10-9-17a9 9 0 0 1 18 0c0 7-9 17-9 17z" fill="none" stroke="#fff" stroke-width="2.5"/><circle cx="20" cy="15" r="3.5" fill="#fff"/><path d="M6 36h28" stroke="#fff" stroke-width="2.5"/></svg></div>
  <div class="abs f-text" style="left:558px"><h4>ADDRESS :</h4><p class="small">Lorem ipsum dolor sit<br>amet, consectetur</p></div>

  <div class="abs f-icon" style="left:743px"><svg width="42" height="40" viewBox="0 0 42 40"><rect x="4" y="8" width="30" height="22" fill="none" stroke="#fff" stroke-width="2.5"/><path d="M4 8l15 12 15-12" fill="none" stroke="#fff" stroke-width="2.5"/><circle cx="33" cy="30" r="6" fill="#fff"/></svg></div>
  <div class="abs f-text" style="left:855px"><h4>Email :</h4><p>info@brindleworks.example</p></div>

  <div class="abs f-links">Home<span>|</span>Services<span>|</span>Industries<span>|</span>About<span>|</span>Reviews<span>|</span>Contact</div>
  <div class="abs f-social"><span></span><span></span><span></span><span></span></div>
  <div class="abs copyright">&copy; 2019 Brindle Works Australia | All rights reserved.</div>
</footer>

</body>
</html>
```